brightwave pools cards

i need to create a design to use on my business cards,brochures and as a letterhead. i am a new swimming pool renovation business named BRIGHTWAVE POOLS. I require a smart professional deign to reflect that my business is the best in the industry.
should include something like.... Brightwave Pools ABN - 71508246913
residential pool renovation specialists
specialising in the art of - fully tiled pools
- waterline tiles
- natural stone pool copings
and outdoor areas - concrete slabs - detailed mosaic work - pool lighting and water features - pool painting

marcus - 0431928604 leonard -0467203851 brightwavepoolsco@tidelmail.com

the design could feature - water, natural stone (travertine, sandstone etc), something to personafy the word imagine.
looking foward to seeing some ideas... cheers heaps marcus

```html
<!DOCTYPE html>
<html lang="en">
<head>
<meta charset="utf-8">
<title>Brightwave Pools – Business Cards</title>
<link rel="stylesheet" href="https://fonts.googleapis.com/css2?family=Questrial&display=swap">
<style>
  :root {
    --page-bg: #ffffff;
    --card-white: #ffffff;
    --card-mist: #d9eefb;
    --card-sky: #bfe3f7;
    --band-deep: #1f86d6;
    --band-light: #55b6ee;
    --band-edge: #cdeafb;
    --brand-blue: #2b8fdc;
    --back-deep: #0f5fb5;
    --back-mid: #1b7fd0;
    --back-light: #4fb2ec;
    --text-white: #ffffff;
    --card-shadow: rgba(20, 60, 110, 0.18);
  }

  * { box-sizing: border-box; margin: 0; padding: 0; }

  html, body {
    width: 1200px;
    height: 900px;
    overflow: hidden;
    background: var(--page-bg);
    font-family: "Questrial", "Century Gothic", sans-serif;
  }

  .card-sheet {
    position: relative;
    width: 1200px;
    height: 900px;
  }

  .card {
    position: absolute;
    top: 285px;
    width: 540px;
    height: 330px;
    border-radius: 26px;
    overflow: hidden;
    box-shadow: 0 14px 30px var(--card-shadow);
  }

  /* Front of card */
  .card-front {
    left: 40px;
    background: linear-gradient(180deg, var(--card-sky) 0%, var(--card-white) 45%, var(--card-white) 62%);
  }

  .brand-name {
    position: absolute;
    top: 72px;
    left: 0;
    width: 100%;
    text-align: center;
    color: var(--brand-blue);
    font-size: 50px;
    line-height: 1.1;
    letter-spacing: 4px;
  }

  .brand-name .brand-line-two {
    display: block;
    font-size: 50px;
    letter-spacing: 26px;
    padding-left: 26px;
  }

  .contact-band {
    position: absolute;
    left: 0;
    top: 218px;
    width: 100%;
    height: 80px;
    background: linear-gradient(180deg, var(--band-light) 0%, var(--band-deep) 100%);
    color: var(--text-white);
    text-align: center;
    padding-top: 10px;
  }

  .contact-band::after {
    content: "";
    position: absolute;
    left: 0;
    top: 80px;
    width: 100%;
    height: 40px;
    background: var(--band-edge);
  }

  .contact-people {
    display: flex;
    justify-content: center;
    gap: 36px;
    font-size: 17px;
    margin-bottom: 6px;
  }

  .contact-email {
    font-size: 17px;
  }

  /* Back of card */
  .card-back {
    left: 620px;
    background: linear-gradient(160deg, var(--back-deep) 0%, var(--back-mid) 50%, var(--back-light) 100%);
  }

  .wave-decoration {
    position: absolute;
    right: -40px;
    top: 0;
    width: 340px;
    height: 100%;
    background: radial-gradient(ellipse at 70% 55%, rgba(255, 255, 255, 0.32) 0%, rgba(255, 255, 255, 0.08) 45%, rgba(255, 255, 255, 0) 70%);
  }

  .services {
    position: relative;
    padding: 52px 0 0 36px;
    color: var(--text-white);
    font-size: 17px;
    line-height: 1.22;
  }

  .services-intro {
    margin-bottom: 22px;
  }

  .services-list {
    list-style: none;
  }
</style>
</head>
<body>
  <main class="card-sheet">
    <section class="card card-front" aria-label="Business card front">
      <h1 class="brand-name">BRIGHTWAVE<span class="brand-line-two">POOLS</span></h1>
      <div class="contact-band">
        <p class="contact-people">
          <span>Marcus - 0431928604</span>
          <span>Leonard -0467203851</span>
        </p>
        <p class="contact-email">brightwavepoolsco@tidelmail.com</p>
      </div>
    </section>

    <section class="card card-back" aria-label="Business card back">
      <div class="wave-decoration" role="img" aria-label="Flowing white line wave pattern with sparkles over blue water"></div>
      <div class="services">
        <p class="services-intro">residential pool renovation specialists<br>specialising in the art of</p>
        <ul class="services-list">
          <li>fully tiled pools</li>
          <li>waterline tiles</li>
          <li>natural stone pool copings and outdoor areas</li>
          <li>concrete slabs</li>
          <li>detailed mosaic work</li>
          <li>pool lighting and water features</li>
          <li>pool painting</li>
        </ul>
      </div>
    </section>
  </main>
</body>
</html>
```